KVAP Property Flyer - For Support Coordinators

Revamping our current brochures and social media posts for our properties. We need a clearer, simpler design that would be designed for Support Coordinators. Attached is our current brochure for reference.

Key details to highlight would include:
- Type of property: Studio Apartments with Psychosocial Disability Support located in Inner West
- Accommodation features
- Services

Our logo is also attached, please make the brochure with similar branding colours and fonts.

Designs look the same

Sick

Font styles to use
Sans Serif
Other font styles liked:
• Montserrat Light and Montserrat Semi Bold

Colors
0054AA
0677BA
7BADD7
CADEEF
E8F1F8

Requirements
Nice to have
• Please refer to this style guide: https://slides.trovelmark.com/deck/8TkwPzLmRd5VbQx2NcYh4GfJs7AeUo9WiKnBrMp3tZq/view?mode=shared

```html
<!DOCTYPE html>
<html lang="en">
<head>
<meta charset="utf-8">
<title>Kindred Haven Care – Larkfield Studio Apartments Flyer</title>
<link rel="stylesheet" href="https://fonts.googleapis.com/css2?family=Open+Sans:wght@300;400;600;700&family=Montserrat:wght@400;600;700&display=swap">
<style>
:root{
  --sky:#21a0dc;
  --sky-light:#6fcbe8;
  --navy:#2a2d3a;
  --ink:#333;
  --white:#fff;
  --orange:#e8762b;
  --photo-light:#e9ecef;
  --photo-mid:#c9ced3;
  --photo-dark:#5c6168;
}
*{margin:0;padding:0;box-sizing:border-box}
html,body{width:1200px;height:1200px;overflow:hidden;background:#fff}
body{position:relative;font-family:"Open Sans",Arial,sans-serif;color:var(--ink)}
.page{position:absolute;width:388px;height:549px;background:var(--white);box-shadow:0 2px 8px rgba(0,0,0,.18);overflow:hidden}
.page--cover{left:172px;top:42px}
.page--gallery{left:627px;top:42px}
.page--transport{left:172px;top:612px}
.page--emergency{left:627px;top:612px}

/* cover */
.cover-address{height:25px;display:flex;align-items:center;justify-content:center;font-family:Montserrat,sans-serif;font-size:10.5px;letter-spacing:2.4px;color:#222}
.cover-hero{position:relative;height:361px;background:linear-gradient(180deg,#4ea6e0 0%,#8cc4ea 35%,#3a3d42 60%,#6b5a4a 85%,#8a8a86 100%)}
.cover-mark{position:absolute;left:58px;top:34px;width:44px;height:44px;border-radius:50%;background:var(--sky-light)}
.cover-brand{position:absolute;left:24px;top:90px;font-size:13px;line-height:16px;font-weight:400;color:var(--white);letter-spacing:.5px;white-space:nowrap}
.cover-suburb{position:absolute;left:20px;top:114px;font-size:33px;line-height:40px;font-weight:700;color:var(--white);letter-spacing:.5px;white-space:nowrap}
.cover-tagline{height:44px;background:var(--sky);color:var(--white);font-weight:300;font-size:15.5px;line-height:19px;padding:3px 21px}
.cover-welcome{height:119px;background:var(--navy);color:#e8e8ea;padding:10px 25px}
.cover-welcome h2{font-size:10.5px;line-height:14px;font-weight:600;color:var(--white);margin-bottom:3px}
.cover-welcome p{font-size:7.6px;line-height:11.8px}
.cover-welcome p+p{margin-top:10px}

/* gallery */
.gallery{position:relative;height:329px}
.photo{position:absolute;background:linear-gradient(135deg,var(--photo-light),var(--photo-mid) 60%,var(--photo-dark))}
.facilities{height:220px;background:var(--sky);color:var(--white);padding:34px 6px 0 19px}
.facility-cols{display:grid;grid-template-columns:194px 1fr}
.facility-col h3{font-size:10.4px;font-weight:600;display:inline-block;padding-bottom:6px;border-bottom:1px solid var(--white);margin-bottom:10px;white-space:nowrap}
.facility-item{display:flex;align-items:center;gap:5px;font-size:7.4px;line-height:9.5px;margin-bottom:10px}
.facility-item svg{flex:none}
.contact-bar{margin:30px 3px 0;border-top:1px solid rgba(255,255,255,.8);padding-top:8px;display:flex;justify-content:space-between;font-size:5.2px}
.contact-bar span{display:flex;align-items:center;gap:3px}
.contact-bar i{display:inline-block;width:7px;height:7px;border:1px solid currentColor;border-radius:50%}

/* transport */
.transport-head{height:40px;background:var(--navy);color:var(--white);font-family:Montserrat,sans-serif;font-weight:600;font-size:11.5px;letter-spacing:3.4px;display:flex;align-items:center;justify-content:center}
.map{position:absolute;left:10px;top:40px;width:369px;height:228px;background:linear-gradient(160deg,#eef0ef,#e4e7e5 50%,#f1e9c8)}
.walk-note{position:absolute;top:282px;left:0;width:100%;text-align:center;font-size:6.7px;font-weight:700;color:var(--sky);letter-spacing:-.3px}
.nearby{position:absolute;left:11px;top:292px;width:367px;height:54px;border:1px dashed #555;padding:4px 7px;display:grid;grid-template-columns:1fr 1fr;column-gap:20px;font-size:7.3px;line-height:9px}
.nearby-item{display:flex;gap:4px;margin-bottom:6.5px}
.nearby b{font-weight:600}
.nearby i{flex:none;width:8px;height:8px;border:1px solid var(--sky);border-radius:2px;margin-top:1px}
.bus-title{position:absolute;left:18px;top:355px;right:14px;display:flex;align-items:center;gap:6px;font-family:Montserrat,sans-serif;font-size:8.6px;letter-spacing:2.2px;color:var(--orange);font-weight:600}
.bus-title::after{content:"";flex:1;height:1px;background:var(--sky)}
.bus-table{position:absolute;left:19px;top:366px;width:353px;font-size:7.4px}
.bus-row{display:flex;align-items:center;height:15.7px;border-bottom:1px solid #ddd}
.bus-row .stop{margin-left:auto;width:222px}
.stop-dot{width:10px;height:10px;border-radius:50%;background:var(--sky);color:#fff;font-size:5.5px;font-weight:700;display:flex;align-items:center;justify-content:center;margin-right:12px}
.route{background:var(--sky);color:#fff;border-radius:6px;padding:0 6px;font-size:6.4px;font-weight:600;margin-right:3px;line-height:9px}
.trips{position:absolute;left:21px;top:434px;width:350px;font-size:6.8px;line-height:8.6px}
.trips p{margin-bottom:8.5px}
.trips strong{color:var(--sky);font-weight:600}
.rail{display:inline-block;width:8px;height:8px;background:var(--orange);vertical-align:-1px;margin:0 3px}
.line{background:var(--orange);color:#fff;padding:0 2px;font-size:6px;margin:0 3px}
.transport-foot{position:absolute;left:0;bottom:0;width:100%;height:10px;background:var(--navy)}

/* emergency */
.emergency-panel{position:absolute;left:10px;top:10px;right:10px;bottom:10px;background:linear-gradient(180deg,#3a3a3c 0%,#2a2a2c 40%,#1e1e20 100%);color:#f2f2f2}
.emergency-panel h2{position:absolute;left:31px;top:36px;right:24px;font-family:Montserrat,sans-serif;font-size:17px;font-weight:600;letter-spacing:4.3px;padding-bottom:6px;border-bottom:1px solid #666;white-space:nowrap}
.emergency-list{position:absolute;left:32px;top:76px;right:2px;font-size:8.9px;line-height:11px;list-style:none}
.emergency-list li{margin-bottom:11px;white-space:nowrap}
.emergency-list b{font-weight:600}
.emergency-list .indent{display:block;padding-left:211px}
.emergency-brand{position:absolute;right:38px;top:382px;display:flex;flex-direction:column;align-items:center;gap:8px;font-size:10px;letter-spacing:.6px;color:#e6e6e6}
.emergency-brand::before{content:"";width:38px;height:38px;border-radius:50%;background:var(--sky-light)}
.emergency-panel .contact-bar{position:absolute;left:21px;right:16px;bottom:34px;margin:0;border-top:1px solid #ddd;color:#ddd}
</style>
</head>
<body>

<section class="page page--cover">
  <div class="cover-address">27 Wren Street, Larkfield NSW 2090</div>
  <div class="cover-hero" role="img" aria-label="Photo of the modern dark brick apartment building with planted balconies next to a red brick house under blue sky">
    <div class="cover-mark"></div>
    <div class="cover-brand">KINDRED HAVEN CARE</div>
    <div class="cover-suburb">LARKFIELD</div>
  </div>
  <div class="cover-tagline">Studio Apartments for people with a<br>psychosocial disability</div>
  <div class="cover-welcome">
    <h2>WELCOME TO LARKFIELD</h2>
    <p>Located in the heart of Larkfield, our new 20 self-contained studio apartments which have a kitchen with fridge, small stove top and microwave. It has a single bed, tv, dining table and bathroom. Some apartments have small balconies, and some have decks overlooking the bustling suburb.</p>
    <p>Situated a 5 minute walk to Larkfield Train Station, and other public transport.</p>
  </div>
</section>

<section class="page page--gallery">
  <div class="gallery">
    <div class="photo" style="left:11px;top:21px;width:118px;height:79px" role="img" aria-label="Studio with kitchenette and balcony door"></div>
    <div class="photo" style="left:134px;top:21px;width:117px;height:79px" role="img" aria-label="White studio entry and kitchen"></div>
    <div class="photo" style="left:256px;top:21px;width:120px;height:79px" role="img" aria-label="Bedroom with balcony railing"></div>
    <div class="photo" style="left:11px;top:105px;width:180px;height:119px" role="img" aria-label="Single bed and dining table"></div>
    <div class="photo" style="left:198px;top:105px;width:180px;height:119px" role="img" aria-label="Kitchenette with microwave"></div>
    <div class="photo" style="left:12px;top:231px;width:118px;height:81px" role="img" aria-label="Studio room with bed and kitchen"></div>
    <div class="photo" style="left:137px;top:231px;width:116px;height:81px" role="img" aria-label="Open fridge and cooktop"></div>
    <div class="photo" style="left:260px;top:231px;width:119px;height:81px" role="img" aria-label="Bright room with glass balcony doors"></div>
  </div>
  <div class="facilities">
    <div class="facility-cols">
      <div class="facility-col">
        <h3>COMMUNITIES &amp; FACILITIES</h3>
        <div class="facility-item"><svg width="15" height="15" viewBox="0 0 16 16" fill="none" stroke="#fff"><circle cx="8" cy="8" r="6"/><path d="M2 2v6M14 2v12"/></svg>Close to shop, cafe, and public transport</div>
        <div class="facility-item"><svg width="15" height="15" viewBox="0 0 16 16" fill="#fff"><path d="M8 14 2 8a3.5 3.5 0 0 1 6-4 3.5 3.5 0 0 1 6 4z"/></svg>Local GP Practice and Destistry</div>
        <div class="facility-item"><svg width="15" height="15" viewBox="0 0 16 16" fill="none" stroke="#fff"><circle cx="8" cy="8" r="6"/><circle cx="8" cy="8" r="2.5"/></svg>Commercial Space for Enterprise</div>
      </div>
      <div class="facility-col">
        <h3>FEATURES &amp; SERVICES</h3>
        <div class="facility-item"><svg width="15" height="15" viewBox="0 0 16 16" fill="none" stroke="#fff"><circle cx="8" cy="8" r="6.5"/><path d="M8 4v4l3 2"/></svg>24/7 Video-Intercom &amp; on site support</div>
        <div class="facility-item"><svg width="15" height="15" viewBox="0 0 16 16" fill="none" stroke="#fff"><circle cx="8" cy="2.5" r="1.5"/><path d="M8 5v5h4l1 4"/><circle cx="7" cy="11" r="3.5"/></svg>Disability access walkways &amp;<br>bathroom</div>
        <div class="facility-item"><svg width="15" height="15" viewBox="0 0 16 16" fill="none" stroke="#fff"><circle cx="8" cy="6.5" r="5"/><path d="M6 11.5v3h4"/></svg>Irained &amp; experienced staff in<br>psychosocial disability</div>
      </div>
    </div>
    <div class="contact-bar">
      <span><i></i>1300 555 014</span>
      <span><i></i>info@kindredhaven.example</span>
      <span><i></i>www.kindredhaven.example</span>
      <span><i></i>kindredhaven_homes</span>
    </div>
  </div>
</section>

<section class="page page--transport">
  <div class="transport-head">Public Transport, Shops &amp; Facilities</div>
  <div class="map" role="img" aria-label="Street map around 27 Wren St showing Larkfield Station, bus stops, shops and routes to Harbour Market Plaza and Riverside Metro"></div>
  <p class="walk-note">LESS THAN 5MIN WALK TO VARIOUS RESTAURANTS, CAFES AND OTHER SHOPS IN YOUR LOCAL AREA.</p>
  <div class="nearby">
    <div class="nearby-col">
      <div class="nearby-item"><i></i><span><b>Larkfield Pharmacy</b> = 1 Min Walk</span></div>
      <div class="nearby-item"><i></i><span><b>FreshMart - Larkfield</b> = 2 Min Walk</span></div>
      <div class="nearby-item"><i></i><span><b>Pulse Fitness 24/7 Larkfield</b> = 2 Min Walk</span></div>
    </div>
    <div class="nearby-col">
      <div class="nearby-item" style="margin-bottom:3px"><i></i><span><b>Larkfield Family Medical Centre</b> = 4 Min Walk</span></div>
      <div class="nearby-item"><i></i><span><b>Larkfield Dental Practice</b> = 1 Min Walk</span></div>
    </div>
  </div>
  <div class="bus-title">Local Bus Routes</div>
  <div class="bus-table">
    <div class="bus-row"><span class="stop-dot">1</span><span class="route">428</span><span class="stop">Kingsway Rd at Oak St | 5 Min Walk</span></div>
    <div class="bus-row"><span class="stop-dot">2</span><span class="route">445</span><span class="stop">Baxter St opp Wren St | 1 Min Walk</span></div>
    <div class="bus-row"><span class="stop-dot">3</span><span class="route">412</span><span class="route">445</span><span class="route">N50</span><span class="stop">Larkfield Station at Hawthorn St | 3 Min Walk</span></div>
    <div class="bus-row"><span class="stop-dot">4</span><span class="route">428X</span><span class="route">445</span><span class="stop">Kingsway Rd before Ridgeway Rd | 3 Min Walk</span></div>
  </div>
  <div class="trips">
    <p><strong>Larkfield to Riverside Metro (17 mins)</strong> = 5 min walk to <span class="stop-dot" style="display:inline-flex;margin:0 2px;vertical-align:-2px">1</span><span class="route">428</span> 6 stops to Elmvale<br>Park (7 mins) &gt; 5 min walk Riverside Metro</p>
    <p><strong>Larkfield to Central (15 mins)</strong> = 4 min walk to <span class="rail"></span> Larkfield &gt; <span class="line">T2</span> Platform 1<br>&gt; 5 stops to Central (11 mins)</p>
    <p><strong>Larkfield to Harbour Market Plaza (14mins)</strong> = 1 min walk to <span class="stop-dot" style="display:inline-flex;margin:0 2px;vertical-align:-2px">2</span><span class="route">445</span> &gt; 9 stops to<br>Mill St (12 mins) &gt; 1 min walk Harbour Market Plaza</p>
    <p><strong>Larkfield to Northgate (8 mins)</strong> = 4 min walk to <span class="rail"></span> Larkfield &gt; <span class="line">T2</span> Platform 1<br>&gt; 2 stops to Northgate (4 mins)</p>
  </div>
  <div class="transport-foot"></div>
</section>

<section class="page page--emergency">
  <div class="emergency-panel" role="img" aria-label="Dark upward view between tall city towers">
    <h2>Emergency Contact List</h2>
    <ul class="emergency-list">
      <li><b>National Emergency Line:</b> 000</li>
      <li><b>Larkfield Police Station:</b> (02) 5550 0199 | Open 24 hrs</li>
      <li><b>Larkfield Family Medical Centre:</b> (02) 5550 8207 | Mon - Fri | 9am - 9pm <span class="indent">| Sat - Sun | 9am - 1pm</span></li>
      <li><b>Harbourside West Council:</b> (02) 5550 5000 | Open Mon - Fri | 8.30am - 5pm</li>
      <li><b>Bayview General Hospital :</b> (02) 5550 6111 | Open 24 hrs</li>
      <li><b>HAVENSDA:</b> (1300) 555 014 | Open Mon - Fri | 9am - 5.30p</li>
    </ul>
    <div class="emergency-brand">KINDRED HAVEN CARE</div>
    <div class="contact-bar">
      <span><i></i>1300 555 014</span>
      <span><i></i>info@kindredhaven.example</span>
      <span><i></i>www.kindredhaven.example</span>
      <span><i></i>kindredhaven_homes</span>
    </div>
  </div>
</section>

</body>
</html>
```